We are Australias only review site for pet boarding (online business)

We need a flyer created with our logo and banner on the front page, and instructions on how to "write a review" on the reverse side (which will have screen shots).

We want to include our URL: www.kennelquillhub.com.au
We would like to also add a tagline "Stop. Review. Our Pets need you!" (without the quote marks) somewhere on the design.

```html
<!DOCTYPE html>
<html lang="en">
<head>
<meta charset="utf-8">
<title>KennelQuillHub Flyer</title>
<link rel="stylesheet" href="https://fonts.googleapis.com/css2?family=Poppins:wght@600&family=Open+Sans:wght@400;500;700;800&display=swap">
<style>
  :root {
    --green: #86b83a;
    --purple: #8a3f96;
    --red: #e8232a;
    --ink: #111111;
    --white: #ffffff;
    --pug: #cbb08c;
    --pug-dark: #8a7560;
    --cat: #c9c8c4;
    --cat-light: #e6e5e2;
    --floor: #f1f1f1;
    --kitten-grey: #a49d94;
    --pup-black: #2f2f33;
    --kitten-cream: #ddcbb6;
    --kitten-brown: #7d6c5f;
  }
  html, body {
    margin: 0;
    padding: 0;
    overflow: hidden;
    background: var(--white);
  }
  .flyer {
    position: relative;
    width: 851px;
    height: 1200px;
    overflow: hidden;
    background: var(--white);
    font-family: "Open Sans", Arial, sans-serif;
  }
  .flyer-frame {
    position: absolute;
    left: 20px;
    top: 20px;
    width: 811px;
    height: 1157px;
    box-sizing: border-box;
    border: 6px solid var(--green);
    z-index: 5;
    pointer-events: none;
  }
  .brand-dot {
    position: absolute;
    left: 55px;
    top: 62px;
    width: 160px;
    height: 160px;
    border-radius: 50%;
    background: var(--green);
  }
  .brand-name {
    position: absolute;
    left: 280px;
    top: 100px;
    margin: 0;
    font-family: "Poppins", Arial, sans-serif;
    font-weight: 600;
    font-size: 66px;
    line-height: 1;
    letter-spacing: -1.5px;
    color: var(--purple);
  }
  .hero-photo {
    position: absolute;
    left: 50px;
    top: 300px;
    width: 776px;
    height: 370px;
    background:
      radial-gradient(ellipse 34% 46% at 30% 48%, var(--pug) 0%, var(--pug) 55%, rgba(203,176,140,0) 100%),
      radial-gradient(ellipse 40% 34% at 70% 52%, var(--cat) 0%, var(--cat-light) 55%, rgba(230,229,226,0) 100%),
      linear-gradient(180deg, var(--white) 0%, var(--white) 70%, var(--floor) 82%, var(--white) 100%);
  }
  .tagline {
    position: absolute;
    left: 0;
    top: 655px;
    width: 851px;
    height: 225px;
  }
  .tagline svg { display: block; }
  .tag-big {
    font-family: "Open Sans", Arial, sans-serif;
    font-weight: 800;
    font-size: 54px;
    letter-spacing: -1px;
    fill: var(--ink);
  }
  .tag-plea {
    font-family: "Open Sans", Arial, sans-serif;
    font-weight: 400;
    font-size: 25px;
    fill: var(--ink);
  }
  .claim-band {
    position: absolute;
    left: 26px;
    top: 910px;
    width: 799px;
    height: 88px;
    background: var(--purple);
  }
  .claim-text {
    position: absolute;
    left: 0;
    top: 10px;
    width: 880px;
    margin: 0;
    text-align: center;
    font-weight: 500;
    font-size: 19px;
    color: var(--white);
    text-shadow: 0 1px 2px rgba(0, 0, 0, 0.55);
    z-index: 3;
  }
  .pets-photo {
    position: absolute;
    left: 64px;
    top: 945px;
    width: 722px;
    height: 221px;
    z-index: 2;
    background:
      linear-gradient(90deg,
        rgba(255,255,255,0) 0%,
        var(--kitten-grey) 5%, var(--kitten-grey) 13%,
        rgba(255,255,255,0) 18%,
        var(--pup-black) 22%, var(--pup-black) 33%,
        rgba(255,255,255,0) 38%,
        var(--kitten-cream) 43%, var(--kitten-cream) 53%,
        rgba(255,255,255,0) 57%,
        var(--pup-black) 61%, var(--pup-black) 72%,
        rgba(255,255,255,0) 77%,
        var(--kitten-brown) 82%, var(--kitten-brown) 92%,
        rgba(255,255,255,0) 100%);
    -webkit-mask-image: linear-gradient(180deg, rgba(0,0,0,0) 0%, #000 22%, #000 100%);
    mask-image: linear-gradient(180deg, rgba(0,0,0,0) 0%, #000 22%, #000 100%);
  }
</style>
</head>
<body>
  <main class="flyer">
    <div class="brand-dot"></div>
    <h1 class="brand-name">KennelQuillHub</h1>

    <div class="hero-photo" role="img" aria-label="Photo of a fawn pug lying beside a contented silver tabby cat on a glossy white floor"></div>

    <div class="tagline">
      <svg width="851" height="225" viewBox="0 0 851 225" aria-label="Stop. Review. Our pets need you!">
        <polygon points="262,0 595,0 595,225 262,225" fill="var(--green)"/>
        <polygon points="93,112 157,0 262,0 327,112 262,225 157,225" fill="var(--red)"/>
        <polygon points="540,112 590,0 698,0 757,112 698,225 590,225" fill="var(--purple)"/>
        <text class="tag-big" x="134" y="132">STOP.</text>
        <text class="tag-big" x="318" y="132">Review.</text>
        <text class="tag-plea" x="575" y="102">Our pets</text>
        <text class="tag-plea" x="575" y="136">need you!</text>
      </svg>
    </div>

    <div class="claim-band">
      <p class="claim-text">Australia’s only review site for pet boarding</p>
    </div>

    <div class="pets-photo" role="img" aria-label="Photo of a row of kittens and French bulldog puppies sitting side by side"></div>

    <div class="flyer-frame"></div>
  </main>
</body>
</html>
```